New Website for IT Services Business

We need an uncoded web design for a new company based in Australia called "Falcon IT". We offer specialised point of sale (POS) support to the hospitality industry. We already support hundreds of cafes and restaurants. We are also about to launch and promote a range of new services with the offering of General IT Support being the most important. Other additional services to be offered are Falcon Vault Storage, reselling and supporting Corvel Shieldware and Trelmo Suite.

We have a logo design and our colour scheme is based on the logo with the addition of charcoal grey (see attached logos). We want the pages to reflect precision and efficiency with sharp characteristics. It must be professional but playful/fun elements are encouraged.

Our target audience is restaurant and cafe owners who are interested in finding high quality POS and IT support for their business.

The main call to action on the home page should be either 'Let's Meet For Coffee!' or 'Find out more (by completing a form)'. If you are unsure about what the general text should say then you can use 'Lorem Ipsum' where required.

The site must be viewable at different resolutions and on smart phones and tablets.

The website structure will be quite simple. We require:
- one impressive landing page. Visitors will quickly determine our services and that we provide a very high level of service while also offering value for money. Obviously a clear list of links (however/wherever you like) to the other pages.
- Simple pages with a similar layout for the following:
- Services - "POS & IT Support for the Hospitality Industry" being the main one. With complementary services also listed. Another call to action on this page with the option of 'Let's Meet For Coffee' or a "More information/Pricing" form to be completed by the visitor.
- Products - will be a small online storefront for a few simple products.
- About - Business background. 2x Directors with a photo and brief Bio.
- Downloads - A list of free files to download. Includes remote access client software.
- Contact Us - Mailing address, Email addresses and Support phone number.

Please feel free to ask any questions about the design. I will assist as much as possible.

Thank you for viewing. We promise to give constructive feedback to every person who submits a design. Thank you so much.

Target Market(s)

Restaurant and Cafe owners.

Industry/Entity Type

Hospitality

Requirements
Must have
• - Viewable on different resolutions and on smart phones and tablets.
- Clear call to action of EITHER 'Let's Meet For Coffee' or a "More information/Pricing" form to be completed by the visitor.

```html
<!DOCTYPE html>
<html lang="en">
<head>
<meta charset="utf-8">
<title>Falcon IT – Smart IT Solutions</title>
<link rel="stylesheet" href="https://fonts.googleapis.com/css2?family=Arimo:wght@400;700&family=Cinzel:wght@400;600&family=Open+Sans:wght@400;600;700&display=swap">
<style>
:root{
  --red:#c8282d;
  --red-dark:#9e1e22;
  --charcoal:#3d3d3d;
  --text:#666;
  --heading:#777;
  --band:#dcdcdc;
  --panel:#f2f2f2;
  --field:#efefef;
  --white:#fff;
}
*{box-sizing:border-box;margin:0;padding:0}
html,body{width:819px;height:1200px;overflow:hidden;background:var(--white)}
body{position:relative;font-family:Arimo,Arial,sans-serif;color:var(--text)}
.abs{position:absolute}

.site-header{position:absolute;left:0;top:0;width:819px;height:110px}
.brand{left:48px;top:36px;display:flex;align-items:center;gap:8px}
.brand-dot{width:32px;height:32px;border-radius:50%;background:var(--red)}
.brand-name{font-family:"Open Sans",sans-serif;font-weight:700;font-size:22px;color:#222}
.main-nav a{position:absolute;top:46px;font-family:"Open Sans",sans-serif;font-weight:600;font-size:13px;color:#333;text-decoration:none}
.main-nav a.active{color:var(--red)}
.header-rule{left:0;top:98px;width:819px;height:5px;background:#d5d5d5}
.header-rule::before{content:"";position:absolute;left:0;top:0;width:218px;height:5px;background:var(--red)}

.hero{left:0;top:110px;width:819px;height:321px;overflow:hidden}
.hero-photo{position:absolute;inset:0;
  background:
    radial-gradient(ellipse 140px 200px at 600px 150px,rgba(238,214,190,.85),rgba(238,214,190,0) 70%),
    radial-gradient(ellipse 120px 160px at 740px 170px,rgba(40,26,20,.85),rgba(40,26,20,0) 75%),
    radial-gradient(ellipse 200px 90px at 250px 260px,rgba(210,170,130,.55),rgba(210,170,130,0) 70%),
    radial-gradient(ellipse 220px 120px at 160px 70px,rgba(70,44,28,.7),rgba(70,44,28,0) 75%),
    linear-gradient(90deg,#4e3322 0%,#7c5538 28%,#a27a58 48%,#c9a98a 62%,#8a6850 76%,#2e211c 100%)}
.hero-shade{position:absolute;inset:0;background:linear-gradient(90deg,rgba(30,18,10,.35),rgba(30,18,10,.1) 55%,rgba(0,0,0,0) 70%)}
.hero-title{position:absolute;left:29px;top:50px;font-family:Cinzel,serif;font-weight:600;font-size:38px;color:#f4f0ea;letter-spacing:1.5px;white-space:nowrap}
.hero-tag{position:absolute;left:131px;top:114px;font-family:"Open Sans",sans-serif;font-weight:700;font-size:14px;color:#f4f0ea;letter-spacing:.3px}
.hero-copy{position:absolute;left:108px;top:175px;width:380px;font-size:12px;line-height:16px;color:#fff;white-space:nowrap}
.btn-hero{position:absolute;left:218px;top:262px;width:108px;height:44px;border-radius:3px;background:linear-gradient(#ececec,#b9b9b9);font-size:14px;color:#222;display:flex;align-items:center;justify-content:center}

.launch{left:0;top:431px;width:819px;height:56px;background:var(--band);border-bottom:2px solid #c9c9c9}
.launch h2{position:absolute;left:70px;top:18px;font-weight:400;font-size:19px;color:var(--heading)}
.info-badge{position:absolute;left:686px;top:10px;width:44px;height:44px;border-radius:50%;background:radial-gradient(circle at 40% 30%,#444,#0a0a0a 70%);color:#fff;font:700 24px Georgia,serif;display:flex;align-items:center;justify-content:center}

.offerings{left:0;top:489px;width:819px;height:144px;background:var(--panel);border-bottom:1px solid #ccc}
.offer{position:absolute;top:14px;width:165px}
.offer-icon{width:140px;height:50px;display:flex;align-items:center;justify-content:center}
.offer h3{width:140px;margin-top:8px;font-weight:400;font-size:11.5px;color:#333;text-align:center}
.offer p{margin-top:10px;font-size:9.6px;line-height:11px;color:#444}
.plain-mark{width:34px;height:34px;border-radius:50%}

.intro{left:38px;top:668px;width:372px}
.intro h2,.coffee h2{font-weight:400;font-size:24px;color:var(--heading);text-align:center}
.intro p{margin-top:22px;font-size:11.3px;line-height:16px;color:var(--text)}
.ticks{list-style:none;margin-top:6px;font-size:11.3px;line-height:16px}
.ticks li{display:flex;align-items:center;gap:4px}
.divider{left:422px;top:662px;width:1px;height:218px;background:#e2e2e2}

.coffee{left:483px;top:668px;width:276px}
.coffee h2{margin-left:18px}
.field{position:absolute;left:0;width:276px;display:flex;border:1px solid #c8c8c8;background:var(--field)}
.field span{width:65px;background:linear-gradient(var(--red),var(--red-dark));color:#fff;font-size:13px;padding-left:13px;display:flex;align-items:center}
.field.msg span{align-items:flex-start;padding-top:40px;font-size:11px}
.btn-meet{position:absolute;left:112px;top:241px;width:90px;height:25px;border-radius:3px;background:linear-gradient(#666,#3d3d3d);color:#fff;font-size:14px;display:flex;align-items:center;justify-content:center}

.clients{left:0;top:978px;width:819px;height:94px;background:#f0f0f0}
.client{position:absolute;top:30px;width:130px;text-align:center;font-family:"Open Sans",sans-serif;font-weight:700;font-size:15px;color:#aaa}

.site-footer{left:0;top:1072px;width:819px;height:46px;background:var(--charcoal)}
.site-footer p{position:absolute;right:65px;top:13px;font-size:14px;color:#fff}
</style>
</head>
<body>
<header class="site-header">
  <div class="abs brand"><span class="brand-dot"></span><span class="brand-name">Falcon IT</span></div>
  <nav class="main-nav">
    <a class="active" style="left:326px" href="#">Home</a>
    <a style="left:399px" href="#">Services</a>
    <a style="left:473px" href="#">Products</a>
    <a style="left:562px" href="#">About</a>
    <a style="left:626px" href="#">Downloads</a>
    <a style="left:713px" href="#">Contacts</a>
  </nav>
  <div class="abs header-rule"></div>
</header>

<section class="abs hero">
  <div class="hero-photo" role="img" aria-label="Photo of two women chatting over coffee in a warm, blurred cafe"></div>
  <div class="hero-shade"></div>
  <h1 class="hero-title">SMART IT SOLUTIONS</h1>
  <p class="hero-tag">We Make Your Business Smarter</p>
  <p class="hero-copy">"Lorem ipsum dolor sit amet, consectetur adipisicing elit, sed do<br>&nbsp;eiusmod tempor incididunt ut labore et dolore magna aliqua.<br>Ut enim ad minim veniam, quis nostrud exercitation ullamco<br>&nbsp;laboris nisi ut aliquip ex ea commodo consequat.</p>
  <a class="btn-hero">Let's See Us</a>
</section>

<section class="abs launch">
  <h2>We Are Now Launching Some New Products</h2>
  <div class="info-badge">i</div>
</section>

<section class="abs offerings">
  <div class="offer" style="left:38px">
    <div class="offer-icon"><svg width="60" height="46" viewBox="0 0 60 46"><path d="M12 3h40l-4 30H8z" fill="#3d4a66"/><path d="M14 6h35l-3.4 24H10.6z" fill="#2f5fd8"/><path d="M4 34h50l4 6H2z" fill="#cfd2d6"/><path d="M2 40h56v2H2z" fill="#8b8f95"/></svg></div>
    <h3>IT Support</h3>
    <p>The standard chunk of Lorem Ipsum used since the 1500s is reproduced below for those interested.</p>
  </div>
  <div class="offer" style="left:241px">
    <div class="offer-icon"><svg width="60" height="40" viewBox="0 0 60 40"><defs><linearGradient id="cloudTone" x1="0" y1="0" x2="0" y2="1"><stop offset="0" stop-color="#8fd0ea"/><stop offset="1" stop-color="#3ea2c8"/></linearGradient></defs><path d="M12 36a10 10 0 0 1 0-20 14 14 0 0 1 27-4 11 11 0 0 1 10 24z" fill="url(#cloudTone)"/></svg></div>
    <h3>Falcon Vault Storage</h3>
    <p>The standard chunk of Lorem Ipsum used since the 1500s is reproduced below for those interested.</p>
  </div>
  <div class="offer" style="left:435px">
    <div class="offer-icon"><span class="plain-mark" style="background:var(--red)"></span></div>
    <h3>Corvel Shieldware</h3>
    <p>The standard chunk of Lorem Ipsum used since the 1500s is reproduced below for those interested.</p>
  </div>
  <div class="offer" style="left:630px">
    <div class="offer-icon"><span class="plain-mark" style="background:#4a86c5"></span></div>
    <h3>Trelmo Suite</h3>
    <p>The standard chunk of Lorem Ipsum used since the 1500s is reproduced below for those interested.</p>
  </div>
</section>

<section class="abs intro">
  <h2>Who We Are</h2>
  <p>Sed tempor elit at ligula blandit vestibulum. Duis congue arcu non metus tincidunt adipiscing. Sed in massa at metus congue tincidunt quis eu felis. Morbi euismod consequat nisi, at congue orci vestibulum ac. Etiam consequat convallis mi, id ornare erat ullamcorper nec. Donec quis lorem non elit ultricies rutrum. Donec tristique semper lorem et porta. Vivamus egestas sodales consequat.</p>
  <ul class="ticks">
    <li><svg width="13" height="11" viewBox="0 0 13 11"><path d="M1 6l4 4 7-9" fill="none" stroke="#3fa535" stroke-width="2.4"/></svg>Pellentesque tempor euismod quam in facilisis</li>
    <li><svg width="13" height="11" viewBox="0 0 13 11"><path d="M1 6l4 4 7-9" fill="none" stroke="#3fa535" stroke-width="2.4"/></svg>Integer a odio ac arcu iaculis ultricies quis eu eros</li>
    <li><svg width="13" height="11" viewBox="0 0 13 11"><path d="M1 6l4 4 7-9" fill="none" stroke="#3fa535" stroke-width="2.4"/></svg>tristique aliquet euismod tellus diam ac</li>
  </ul>
</section>
<div class="abs divider"></div>

<section class="abs coffee">
  <h2>Let’s Meet For a Coffee</h2>
  <div class="field" style="top:46px;height:22px"><span>Name</span></div>
  <div class="field" style="top:80px;height:22px"><span>Email</span></div>
  <div class="field msg" style="top:113px;height:115px"><span>Message</span></div>
  <a class="btn-meet">Let’s Meet</a>
</section>

<section class="abs clients">
  <div class="client" style="left:100px">The Loft Kitchen</div>
  <div class="client" style="left:260px">Crust Yard</div>
  <div class="client" style="left:427px">The Loft Kitchen</div>
  <div class="client" style="left:585px">Crust Yard</div>
</section>

<footer class="abs site-footer"><p>Copyrights 2012, INC.</p></footer>
</body>
</html>
```